Homeopathic medicinal cream label design

I am looking for a product label design for a medicinal (cannabis) topical cream to be sold to medical marijuana patients. It is a new product that has not yet established a brand identity. It will be sold in 2 and 4 ounce containers so the design needs to work on a small scale. The design may be used for other branding as well.

Target Market(s)

Medical marijuana users in states where it is legal. The product should appeal to both men and women to promote pain relief in muscles and joints. It can also be used as a massage cream for general relaxation.

Industry/Entity Type

Medical

Font styles to use
Sans Serif

Requirements
Must have
• Something that reflects the company name - The Quiet Heron - and the name of the initial product - Meadow Balm Blend.
• In addition to the name of the company and the name of the product, other information to include would be the volume being sold (e.g. 4 oz.), that it is a topical botanical ointment, and its ingredients (coconut oil, beeswax, soy lecithin, and eight all natural botanical oils - cannabis, lavender, eucalyptus, peppermint, rosemary, cinnamon, clove, and lemon). The label should clearly state that the product is for topical use only.
• The information must fit on the space available on the package. The 4 oz. container's lid has approximately 2 1/8" of surface area. The width of the label on the lid should be approximately 1 7/8". On the container's body, the height of the surface area is approximately 1", and the width is approximately 8 1/2 inches. The width of the label should be around 8 inches to allow room for it to be applied to the container. I have posted a photo of the 4 oz. container and the 2 oz. container. I have also posted a photo of the labeling of some of our competitors with similar products.
Nice to have
• We are thinking of having the logo on the lid of the container, and a circle bordering the lid that may have text in it. (See the "Amber Moth" label attached as an exemplar).
• The label on the body of the container (or maybe on the bottom on the container) would list other information about the product, such as its ingredients and our contact information.

```html
<!DOCTYPE html>
<html lang="en">
<head>
<meta charset="utf-8">
<title>The Quiet Heron – Meadow Balm Blend lid label</title>
<link rel="stylesheet" href="https://fonts.googleapis.com/css2?family=Didact+Gothic&family=Open+Sans:wght@700;800&display=swap">
<style>
  :root {
    --backdrop-light: #d9dadc;
    --backdrop-dark: #a4a6a9;
    --leaf-light: #8cc63f;
    --leaf-mid: #5ea535;
    --leaf-deep: #3b8a2e;
    --ring-gray: #8e8e8e;
    --paper: #ffffff;
    --mark-tint: #d4ebb8;
    --ink-dark: #3a3a3a;
    --title-shadow: #24521a;
  }
  html, body {
    margin: 0;
    padding: 0;
    width: 878px;
    height: 1200px;
    overflow: hidden;
  }
  body {
    position: relative;
    background: radial-gradient(ellipse at center, var(--backdrop-light) 0%, var(--backdrop-light) 35%, var(--backdrop-dark) 100%);
    font-family: "Didact Gothic", sans-serif;
  }
  .lid-label {
    position: absolute;
    left: 129px;
    top: 290px;
    width: 620px;
    height: 620px;
  }
  .lid-label__disc {
    position: absolute;
    inset: 0;
  }
  .lid-label__content {
    position: absolute;
    inset: 0;
    color: var(--paper);
    text-align: center;
  }
  .brand__mark {
    position: absolute;
    top: 54px;
    left: 275px;
    width: 70px;
    height: 70px;
    border-radius: 50%;
    background: var(--mark-tint);
  }
  .brand__name {
    position: absolute;
    top: 144px;
    left: 0;
    right: 0;
    margin: 0;
    font-size: 24px;
    line-height: 28px;
    color: var(--ink-dark);
    letter-spacing: 0.5px;
  }
  .product-name {
    position: absolute;
    top: 0;
    left: 0;
    width: 100%;
    height: 100%;
    margin: 0;
    font-family: "Open Sans", sans-serif;
    line-height: 1;
    text-shadow: 2px 3px 0 var(--title-shadow);
  }
  .product-name__lead {
    position: absolute;
    top: 175px;
    left: 205px;
    display: flex;
    align-items: center;
    gap: 10px;
    font-weight: 700;
    font-size: 40px;
    white-space: nowrap;
  }
  .product-name__dot {
    width: 15px;
    height: 15px;
    border-radius: 50%;
    background: var(--paper);
    box-shadow: 2px 3px 0 var(--title-shadow);
  }
  .product-name__main {
    position: absolute;
    top: 200px;
    left: 0;
    right: 0;
    font-weight: 800;
    font-size: 104px;
    letter-spacing: 2px;
  }
  .ingredients-heading {
    position: absolute;
    top: 308px;
    left: 0;
    right: 0;
    margin: 0;
    font-weight: 400;
    font-size: 35px;
    line-height: 40px;
  }
  .rule {
    position: absolute;
    left: 50%;
    height: 1.5px;
    background: var(--paper);
    transform: translateX(-50%);
  }
  .rule--wide { top: 352px; width: 513px; }
  .rule--short { top: 540px; width: 160px; }
  .ingredients-list {
    position: absolute;
    top: 368px;
    left: 40px;
    right: 40px;
    margin: 0;
    font-size: 25px;
    line-height: 32px;
  }
  .net-weight {
    position: absolute;
    top: 549px;
    left: 50%;
    transform: translateX(-50%);
    margin: 0;
    padding: 0 4px 2px;
    font-size: 25px;
    line-height: 28px;
    border-bottom: 1.5px solid var(--paper);
  }
</style>
</head>
<body>
  <main class="lid-label">
    <svg class="lid-label__disc" viewBox="0 0 620 620" aria-hidden="true">
      <defs>
        <radialGradient id="leaf-fill" cx="45%" cy="20%" r="85%">
          <stop offset="0%" stop-color="#8cc63f"/>
          <stop offset="55%" stop-color="#5ea535"/>
          <stop offset="100%" stop-color="#3b8a2e"/>
        </radialGradient>
      </defs>
      <circle cx="310" cy="310" r="308" fill="#5ea535"/>
      <circle cx="310" cy="310" r="301" fill="#ffffff"/>
      <circle cx="310" cy="310" r="294" fill="#8e8e8e"/>
      <circle cx="310" cy="310" r="290" fill="url(#leaf-fill)"/>
    </svg>

    <div class="lid-label__content">
      <div class="brand">
        <span class="brand__mark"></span>
        <p class="brand__name">The Quiet Heron</p>
      </div>

      <h1 class="product-name">
        <span class="product-name__lead">Meadow Balm<span class="product-name__dot"></span></span>
        <span class="product-name__main">Blend</span>
      </h1>

      <h2 class="ingredients-heading">Ingredients</h2>
      <div class="rule rule--wide"></div>

      <p class="ingredients-list">
        (coconut oil, beeswax, soy lecithin, and<br>
        eight all natural botanical oils – cannabis,<br>
        lavender, eucalyptus, peppermint,<br>
        rosemary,cinnamon, clove,<br>
        and lemon)
      </p>

      <div class="rule rule--short"></div>
      <p class="net-weight">4 oz.</p>
    </div>
  </main>
</body>
</html>
```